Premium Lawn fertiliser packaging - Looking for long term designer

*Update at bottom
I need a carefully considered, bold and professional packaging design for my new premium lawn fertiliser product. This contest is for a detailed front of the stand-up pouch packaging and once I’ve chosen a winner, they’ll be asked to create the layout for the back that links to the front as well. I have a full range of additional products that will also need designs and so I'm looking for someone who can do a great job here and who we can work with long term.

The front should include our logo for Pemberly Turf Supply Direct and be titled “Bloom Vigor Max” "Professional Lawn Fertiliser". The spring fertiliser tag line is "Awaken your lawn: Lush Greening, Lasting Health".
Beneath it, it then needs to include some important usage information and the key benefits along with some suitable graphic.

Key information to include:

Apply March - June
Treats 35-50 m2
16-3-8
+2%MgO + 1% Fe + 2.9% CaO (this is the chemical makeup of the fertiliser and needs to be fairly prominent. If you look at other professional fertiliser packaging, you'll see how it needs to compare).

Key features:
Premium fertiliser, used by professionals
Advanced greening with micro-nutrient complex
Dual action Nitrogen: Instant green boost & continuous feed for 3 months
Child & pet safe

Our brand colours are purple and green. Purple = #592999, Green = 3cb64a / 81d742 / 4d9d44

I think these colours look great against a white background.

Please make sure you look at our website as well to get an idea of our brand: www.pemberlyturfsupply.co.uk

To help, I've attached images of competitors fertiliser packaging that I like the look of. I'm not looking for you to copy but just see what type of thing appeals to me, the standard I'm expecting and what I need to compete against....

In addition, I have also attached some potential images you may wish to try using in your design, although please feel free to use your own if you have something better. For the moment, the images are 'preview' images, but once I decide on a design and we agree on the correct image, I will download and send over a fully licensed version.

*** Update*** When submitting your design, can you submit it in 2 formats: The first as a fully printed custom stand-up pouch and the second as a full-size label stuck onto a standup pouch (whatever colour you think is right for your design - choose white if you are not sure). To explain, I've just discovered we won't be able to get full custom bags printed in time for the first run and so we will have to opt for the design to be printed on labels and fixed onto bags. I therefore need to choose a design that works in both formats as both a label on a standup pouch as well as a fully printed pouch. Many thanks.

Target Market(s)

Domestic home-owners

Industry/Entity Type

Lawn care. NOT AGRICULTURE OR FARMING

Font styles to use
Sans Serif

Requirements
Must have
• Presented in 2 formats - see update at bottom of description
Nice to have
• I quite like designs against a white background, although I’m open to other ideas as well.
Should not have
• Please do not include any people or faces in the design. The text should be solid in colour, so no graduated colour fill in the text or outline text. Please avoid over-busy or cluttered designs.

```html
<!DOCTYPE html>
<html lang="en">
<head>
<meta charset="utf-8">
<title>Bloom Vigor Max – Professional Lawn Fertiliser Label</title>
<link rel="stylesheet" href="https://fonts.googleapis.com/css2?family=Archivo:ital,wght@0,300;0,400;0,700;0,900;1,700;1,800&family=Roboto+Condensed:wght@400;700&display=swap">
<style>
  :root {
    --purple: #592999;
    --purple-deep: #4a2189;
    --green: #3cb64a;
    --green-light: #81d742;
    --green-dark: #4d9d44;
    --gold: #b8923a;
    --white: #ffffff;
    --page: #f3f3f3;
    --ink-soft: #555555;
  }
  * { box-sizing: border-box; margin: 0; padding: 0; }
  html, body {
    width: 1200px; height: 805px; overflow: hidden;
    background: var(--page);
    font-family: "Archivo", sans-serif;
  }
  .canvas {
    width: 1200px; height: 805px;
    display: flex; align-items: center; justify-content: center;
  }
  .label {
    position: relative;
    width: 540px; height: 765px;
    background: var(--white);
    box-shadow: 0 6px 24px rgba(0,0,0,0.12);
    overflow: hidden;
  }

  /* Brand */
  .brand {
    position: absolute; top: 48px; left: 0; right: 0;
    display: flex; align-items: center; justify-content: center; gap: 10px;
  }
  .brand-dot {
    width: 18px; height: 18px; border-radius: 50%;
    background: var(--green);
  }
  .brand-name {
    font-family: "Archivo", sans-serif;
    font-weight: 700; font-size: 21px;
    color: var(--purple-deep);
    letter-spacing: 0.3px;
  }

  /* Title */
  .title {
    position: absolute; top: 96px; left: 76px;
    line-height: 0.9;
  }
  .title-line1 {
    font-weight: 900; font-size: 92px; color: var(--purple);
    letter-spacing: -1px;
  }
  .title-line2 { display: flex; align-items: baseline; gap: 6px; margin-top: 4px; }
  .title-vigor {
    font-weight: 900; font-size: 70px; color: var(--purple);
    letter-spacing: -1px;
  }
  .title-max {
    font-weight: 300; font-size: 74px; color: var(--green);
  }
  .subtitle-bar {
    position: absolute; top: 268px; left: 76px; width: 392px;
    background: var(--green);
    color: var(--white);
    font-family: "Roboto Condensed", sans-serif; font-weight: 700;
    font-size: 25px; text-align: center;
    padding: 3px 0 4px;
  }

  /* Lawn scene */
  .scene {
    position: absolute; top: 318px; left: 0; width: 540px; height: 350px;
    clip-path: polygon(0 34px, 54% 0, 100% 34px, 100% 100%, 0 100%);
    background:
      linear-gradient(180deg, #6f8fa8 0%, #7f9a6c 22%, #5f8a34 40%, #7fb336 60%, #4f8a22 100%);
  }
  .scene-frame {
    position: absolute; top: 312px; left: 0; width: 540px; height: 40px;
  }

  .tagline {
    position: absolute; top: 472px; left: 34px;
    color: var(--white);
    font-style: italic; font-weight: 800;
    font-size: 27px; line-height: 1.1;
    text-shadow: 0 1px 3px rgba(0,0,0,0.35);
  }

  /* Safe badge */
  .safe-badge {
    position: absolute; top: 346px; left: 418px; width: 94px;
    text-align: center;
  }
  .safe-ring {
    width: 86px; height: 86px; margin: 0 auto;
    border-radius: 50%;
    border: 4px solid var(--gold);
    background: var(--white);
    display: flex; align-items: center; justify-content: center;
  }
  .safe-ring-inner {
    width: 60px; height: 60px; border-radius: 50%;
    background: #e8e0f3;
  }
  .safe-word {
    font-weight: 900; font-size: 26px; color: var(--white);
    line-height: 1; margin-top: 4px;
    text-shadow: 0 1px 2px rgba(0,0,0,0.4);
  }
  .safe-for {
    font-weight: 700; font-size: 9px; color: var(--purple);
    background: var(--white); display: inline-block; padding: 0 4px; margin-top: 2px;
  }
  .safe-who {
    font-weight: 700; font-size: 11px; color: var(--purple);
    background: var(--white); padding: 1px 4px; margin-top: 1px;
    display: inline-block;
  }

  /* Info panel */
  .info {
    position: absolute; top: 552px; left: 346px; width: 152px; height: 128px;
  }
  .info svg { position: absolute; inset: 0; }
  .info-body {
    position: relative; padding: 8px 12px 0; color: var(--white);
  }
  .info-apply {
    font-family: "Roboto Condensed", sans-serif; font-weight: 700; font-size: 13px;
    border-bottom: 1px solid rgba(255,255,255,0.5); padding-bottom: 4px;
  }
  .info-treats { font-size: 10px; margin-top: 4px; }
  .info-area { font-weight: 900; font-size: 27px; line-height: 1; }
  .info-area sup { font-size: 13px; }
  .info-npk {
    font-family: "Roboto Condensed", sans-serif; font-size: 18px;
    border-top: 1px solid rgba(255,255,255,0.5); margin-top: 4px; padding-top: 2px;
    text-align: center;
  }
  .info-trace { font-size: 8px; font-weight: 700; text-align: center; margin-top: 2px; }

  /* Feature band */
  .band {
    position: absolute; left: 0; bottom: 24px; width: 540px; height: 100px;
  }
  .band svg { position: absolute; inset: 0; }
  .features {
    position: absolute; left: 20px; right: 20px; bottom: 10px;
    display: flex; gap: 0;
  }
  .feature {
    display: flex; gap: 6px; padding: 0 10px;
    border-right: 1px solid rgba(255,255,255,0.55);
    color: var(--white);
  }
  .feature:last-child { border-right: none; }
  .feature:nth-child(1) { width: 98px; }
  .feature:nth-child(2) { width: 150px; }
  .feature:nth-child(3) { flex: 1; }
  .tick { flex: none; width: 12px; height: 12px; margin-top: 1px; }
  .feature-head { font-weight: 900; font-size: 10.5px; line-height: 1.05; text-transform: uppercase; }
  .feature-head .accent { color: var(--green-light); }
  .feature-text { font-size: 10px; line-height: 1.1; margin-top: 1px; }
</style>
</head>
<body>
<main class="canvas">
  <section class="label" aria-label="Bloom Vigor Max lawn fertiliser label">

    <header class="brand">
      <span class="brand-dot"></span>
      <span class="brand-name">Pemberly Turf Supply Direct</span>
    </header>

    <h1 class="title">
      <div class="title-line1">BLOOM</div>
      <div class="title-line2"><span class="title-vigor">VIGOR</span><span class="title-max">MAX</span></div>
    </h1>
    <div class="subtitle-bar">Professional Lawn Fertiliser</div>

    <div class="scene" role="img" aria-label="Photograph of a lush green lawn in front of a house with trees"></div>
    <svg class="scene-frame" viewBox="0 0 540 40" aria-hidden="true">
      <polyline points="0,40 292,6 540,40" fill="none" stroke="var(--gold)" stroke-width="3"/>
    </svg>

    <p class="tagline">Awaken Your Lawn<br>Lush Greening,<br>Lasting Health</p>

    <div class="safe-badge">
      <div class="safe-ring"><div class="safe-ring-inner"></div></div>
      <div class="safe-word">SAFE</div>
      <div class="safe-for">FOR</div><br>
      <div class="safe-who">PETS&amp;KIDS</div>
    </div>

    <div class="band">
      <svg viewBox="0 0 540 100" preserveAspectRatio="none" aria-hidden="true">
        <polygon points="0,28 292,0 540,28 540,100 0,100" fill="var(--purple)"/>
        <polyline points="0,28 292,0 540,28" fill="none" stroke="var(--gold)" stroke-width="2.5"/>
      </svg>
      <div class="features">
        <div class="feature">
          <svg class="tick" viewBox="0 0 12 12"><polyline points="1,6 5,10 11,2" fill="none" stroke="var(--green-light)" stroke-width="2.4"/></svg>
          <div><div class="feature-head">Premium Fertiliser</div><div class="feature-text">used by professionals</div></div>
        </div>
        <div class="feature">
          <svg class="tick" viewBox="0 0 12 12"><polyline points="1,6 5,10 11,2" fill="none" stroke="var(--green-light)" stroke-width="2.4"/></svg>
          <div><div class="feature-head">Advanced <span class="accent">Greening</span></div><div class="feature-text">with micro-nutrient complex</div></div>
        </div>
        <div class="feature">
          <svg class="tick" viewBox="0 0 12 12"><polyline points="1,6 5,10 11,2" fill="none" stroke="var(--green-light)" stroke-width="2.4"/></svg>
          <div><div class="feature-head">Dual Action Nitrogen</div><div class="feature-text">Instant green boost &amp; continuous feed for 3 months</div></div>
        </div>
      </div>
    </div>

    <div class="info">
      <svg viewBox="0 0 152 128" preserveAspectRatio="none" aria-hidden="true">
        <polygon points="2,2 150,2 150,112 76,126 2,112" fill="rgba(44,110,40,0.82)" stroke="var(--green)" stroke-width="3"/>
      </svg>
      <div class="info-body">
        <div class="info-apply">Apply March - June</div>
        <div class="info-treats">Treats</div>
        <div class="info-area">35-50m<sup>2</sup></div>
        <div class="info-npk">16 - 03 - 08</div>
        <div class="info-trace">2% MgO + 1% Fe + 2.9% CaO</div>
      </div>
    </div>

  </section>
</main>
</body>
</html>
```